Business card for Les Brisants-Corail campsite

HORIZONTAL / 85x55
OBJECTIVE
Create a modern, attractive and memorable business card for the Les Brisants-Corail campsite, located on the Île d'Oléron.
The map should make people want to discover the campsite and immediately convey its world: ocean, holidays, nature and conviviality.
VISUAL IDENTITY
The design must be in the same graphic style as our website:
www.lesbrisants-corail.fr
The site is the main reference for the visual atmosphere: colours, typography, shapes, photographs and general universe.
The map and the site must give the impression of belonging to a single brand identity.
A UNIVERSE TO TRANSMIT
• Île d'Oléron
• Atlantic Ocean
• Seaside
• Direct access to the beaches
• Vacation
• Nature
• Family-friendly and welcoming atmosphere
• Relaxation
DESIRED STYLE
Bright, warm, modern, nautical and natural.
We want a creation with a real personality, immediately recognizable, and not a generic camping business card.
FRONT
Prioritize visual impact with:
• Official logo Les Brisants-Corail
• Île d'Oléron
• A strong evocation of the ocean and holidays
• A short and memorable hook
The designer is free to propose their own hook.
BACK
The Coral Breakers
Villages 1 & 2
22 Rue des Mouettes
17310 Saint-Pierre-d'Oléron
France
Tel.: +33 5 47 12 38 04
www.lesbrisants-corail. fr
Possibility of discreet integration:
Direct access to the beaches
Mobile homes • Pitches • Accommodation
Le Varech Bar-Restaurant
FORMAT
Double-sided card: 85 × 55 mm.
Horizontal orientation
AVOID
• Overly institutional design
• Overloaded map
• Generic "camping" style
• Too many pictograms
• Accumulation of texts
• Modification or distortion of the official logo
• Graphic design unrelated to the website
CREATIVE FREEDOM
We are looking for an original proposal.
The designer can play with the graphic codes of the ocean, waves, sun, beach and Île d'Oléron, while remaining faithful to the visual identity of the site.
The card must be aesthetically pleasing and original enough to make people want to keep it.
The objective:
See the map → think about the ocean and holidays → remember Les Brisants-Corail → discover the campsite.
Target Market(s)
All targets
Industry/Entity Type
Tourisme
Contact Information for Business Card
adresse, téléphone, email, site internet + réseaux sociaux
Look and feel
Each slider illustrates characteristics of the customer's brand and the style your logo design should communicate.

```html
<!DOCTYPE html>
<html lang="en">
<head>
<meta charset="UTF-8">
<title>Les Brisants-Corail – Business Card</title>
<link rel="stylesheet" href="https://fonts.googleapis.com/css2?family=Domine:wght@400;600;700&display=swap">
<style>
  :root {
    --navy: #1c2a3e;
    --navy-deep: #15202f;
    --sky: #5bbde6;
    --sun: #f6e32b;
    --leaf: #a8c62a;
    --leaf-dark: #6f9a2b;
    --white: #ffffff;
    --sea: #2f5a72;
    --canvas: #ffffff;
  }
  html, body {
    margin: 0;
    padding: 0;
    width: 1200px;
    height: 1200px;
    overflow: hidden;
    background: var(--canvas);
  }
  .card {
    position: absolute;
    top: 466px;
    width: 416px;
    height: 269px;
    box-shadow: 6px 8px 10px rgba(0,0,0,0.35);
    overflow: hidden;
  }
  .card--front { left: 139px; }
  .card--back { left: 650px; }
  .card svg { display: block; width: 100%; height: 100%; }
  .brand-name, .label, .feature, .contact { font-family: 'Domine', serif; }
  .brand-name { font-weight: 600; }
  .label { font-weight: 700; letter-spacing: 1px; }
  .feature { font-weight: 600; fill: var(--white); font-size: 12.5px; letter-spacing: 0.4px; }
  .contact { font-weight: 600; fill: var(--white); }
</style>
</head>
<body>

<!-- Front side -->
<div class="card card--front">
  <svg viewBox="0 0 670 434" xmlns="http://www.w3.org/2000/svg">
    <defs>
      <linearGradient id="seaGradient" x1="0" y1="0" x2="0" y2="1">
        <stop offset="0" stop-color="#1c2a3e"/>
        <stop offset="0.45" stop-color="#2f5a72"/>
        <stop offset="1" stop-color="#8a8576"/>
      </linearGradient>
    </defs>
    <rect class="front-bg" width="670" height="434" fill="var(--navy)"/>
    <rect class="front-photo" role="img" aria-label="Photo of Atlantic waves breaking on a sandy beach"
          x="0" y="170" width="670" height="264" fill="url(#seaGradient)"/>

    <g class="front-brand">
      <circle cx="200" cy="98" r="14" fill="var(--sun)"/>
      <text class="brand-name" x="226" y="110" font-size="34" fill="var(--white)">Les Brisants-Corail</text>
    </g>

    <g class="front-tag">
      <rect x="240" y="211" width="208" height="42" rx="7" fill="var(--sun)"/>
      <text class="label" x="344" y="240" font-size="20" text-anchor="middle" fill="var(--navy)">ÎLE D'OLÉRON</text>
    </g>

    <g class="front-waves">
      <path fill="var(--leaf)" d="M0,218 C40,330 130,388 240,390 C400,392 520,286 670,365 L670,434 L0,434 Z"/>
      <path fill="var(--sun)" d="M0,232 C45,345 140,398 250,398 C410,396 520,300 670,380 L670,434 L0,434 Z"/>
      <path fill="var(--sky)" d="M0,262 C55,370 150,410 260,408 C420,404 530,330 670,392 L670,434 L0,434 Z"/>
    </g>
  </svg>
</div>

<!-- Back side -->
<div class="card card--back">
  <svg viewBox="0 0 670 434" xmlns="http://www.w3.org/2000/svg">
    <defs>
      <linearGradient id="campGradient" x1="0" y1="0" x2="1" y2="1">
        <stop offset="0" stop-color="#5f7d2a"/>
        <stop offset="1" stop-color="#3e5e22"/>
      </linearGradient>
      <linearGradient id="duneGradient" x1="0" y1="0" x2="0" y2="1">
        <stop offset="0" stop-color="#7f9c2a"/>
        <stop offset="1" stop-color="#b3a33a"/>
      </linearGradient>
    </defs>
    <rect class="back-bg" width="670" height="434" fill="var(--white)"/>

    <g class="back-brand">
      <circle cx="434" cy="73" r="11" fill="var(--sky)"/>
      <text class="brand-name" x="640" y="80" font-size="20" text-anchor="end" fill="var(--navy)">Les Brisants-Corail</text>
    </g>

    <g class="back-waves">
      <path fill="var(--leaf)" d="M0,180 C20,210 45,228 70,238 L60,246 C35,236 14,222 0,205 Z"/>
      <path fill="var(--navy)" d="M0,212 C60,280 160,302 300,300 C450,296 540,208 670,238 L670,434 L0,434 Z"/>
      <path fill="var(--leaf)" d="M300,296 C430,292 540,222 670,262 L670,290 C560,250 440,288 300,296 Z"/>
      <path fill="var(--leaf)" d="M290,262 L370,254 L300,268 Z"/>
    </g>

    <g class="back-photos">
      <ellipse role="img" aria-label="Aerial photo of the campsite among pine trees"
               cx="110" cy="180" rx="90" ry="128" transform="rotate(-14 110 180)"
               fill="url(#campGradient)" stroke="var(--white)" stroke-width="6"/>
      <ellipse role="img" aria-label="Photo of dune grass overlooking the beach"
               cx="268" cy="200" rx="60" ry="85" transform="rotate(18 268 200)"
               fill="url(#duneGradient)" stroke="var(--white)" stroke-width="6"/>
    </g>

    <g class="back-features">
      <circle cx="25" cy="330" r="2" fill="var(--leaf)"/>
      <text class="feature" x="37" y="334">Direct access to the beaches</text>
      <circle cx="25" cy="355" r="2" fill="var(--leaf)"/>
      <text class="feature" x="37" y="359">Mobile homes</text>
      <circle cx="25" cy="381" r="2" fill="var(--leaf)"/>
      <text class="feature" x="37" y="385">Pitches</text>
      <circle cx="25" cy="405" r="2" fill="var(--leaf)"/>
      <text class="feature" x="37" y="409">Accommodation Le Varech Bar-Restaurant</text>
    </g>

    <g class="back-contact">
      <path fill="none" stroke="var(--leaf)" stroke-width="2" d="M453,332 a5,5 0 1,1 10,0 c0,4 -5,9 -5,9 c0,0 -5,-5 -5,-9 z"/>
      <circle cx="458" cy="332" r="1.6" fill="var(--leaf)"/>
      <text class="contact" x="472" y="332" font-size="10.5">22 Rue des Mouettes</text>
      <text class="contact" x="472" y="346" font-size="10.5">17310 Saint-Pierre-d'Oléron</text>
      <text class="contact" x="472" y="360" font-size="10.5">France</text>

      <g transform="translate(452,375) scale(0.65)">
        <path fill="var(--leaf)" d="M0,0 c2,-2 4,-2 5,0 l2,3 c1,1 0,3 -1,3 c1,3 3,5 6,6 c0,-1 2,-2 3,-1 l3,2 c2,1 2,3 0,5 c-2,2 -5,2 -8,0 c-5,-3 -9,-7 -11,-12 c-1,-3 -1,-5 1,-6 z"/>
      </g>
      <text class="contact" x="472" y="386" font-size="15">+33 5 47 12 38 04</text>

      <circle cx="458" cy="404" r="5" fill="none" stroke="var(--leaf)" stroke-width="1.6"/>
      <ellipse cx="458" cy="404" rx="2" ry="5" fill="none" stroke="var(--leaf)" stroke-width="1.2"/>
      <line x1="453" y1="404" x2="463" y2="404" stroke="var(--leaf)" stroke-width="1.2"/>
      <text class="contact" x="472" y="408" font-size="11">www.lesbrisants-corail. fr</text>
    </g>
  </svg>
</div>

</body>
</html>
```